Label Design for Amber Reed Specialty Coffee Roasters

We are a specialty coffee beans Roasting Shop named "Amber Reed". We pack our beans in stand up poaches of varying sizes. We sell beans both to B2C and B2B and are looking to design stickers that will stand out. Our logo was designed with a black and white background. So far, we have been using white glossy bean bags and came up with a front label design that we would like to use for our labels.
We would like to see the design tweaked to fit both a white bag and a black one.
Currently, the attached front label design does not work on white bags. We would also like to have a back sticker designed that needs to include: 1- a description section for the type of beans used 2- a QR code section

Target Market(s)

Specialty beans in our area are typically liked by the younger generations 40 years and younger. Both male and females drink our coffee with varying income levels. But generally, middle class and above buy our coffee beans.

Requirements
Must have
• We are am looking for a sticker to be placed on a coffee bean bag. The sticker needs to contain the roasting shop's logo and brand name "Amber Reed". Also, the sticker needs to have the following: country name, bean variety, weight (kg), roast date. The sticker needs to have the following specifications on a 5 point Likert scale (Strength, Fruitiness, Earthiness, Brightness). I uploaded a front label design that needs to be tweaked to fit both a white bag and a black one. The current design has owls representing the 5 point Likert scale and part of the shop's logo. We would like to keep that part of the design if possible. Currently, the attached front label design does not work on white bags.
We would also like to have a back sticker designed that needs to include: 1- a description section for the type of beans used 2- a QR code section
Nice to have
• The font that is used in the logo is League Gothic. It is okay to use this font or any other font if you find it more appropriate for the design.

```html
<!DOCTYPE html>
<html lang="en">
<head>
<meta charset="utf-8">
<title>Amber Reed Specialty Coffee Roasters – Front Labels</title>
<link rel="stylesheet" href="https://fonts.googleapis.com/css2?family=League+Gothic&display=swap">
<style>
  :root {
    --backdrop: #c8c9ca;
    --ink: #111111;
    --paper: #ffffff;
    --figure-dark-a: #1a1a1a;
    --figure-dark-b: #3a3a3a;
    --figure-light-a: #ffffff;
    --figure-light-b: #d9d9d9;
  }
  * { box-sizing: border-box; margin: 0; padding: 0; }
  html, body {
    width: 971px; height: 1200px; overflow: hidden;
    background: var(--backdrop);
  }
  .sheet {
    position: relative;
    width: 1003px; height: 1240px;
    transform: scale(0.968); transform-origin: 0 0;
    font-family: "League Gothic", "Oswald", sans-serif;
    letter-spacing: 0.2px;
  }
  .label {
    position: absolute;
    width: 423px; height: 524px;
    border-radius: 26px;
    overflow: hidden;
  }
  .label > * { z-index: 1; }
  .label--dark { background: var(--ink); color: var(--paper); }
  .label--light { background: var(--paper); color: var(--ink); }
  .pos-tl { left: 60px; top: 77px; }
  .pos-tr { left: 521px; top: 77px; }
  .pos-bl { left: 60px; top: 638px; }
  .pos-br { left: 521px; top: 638px; }

  /* brand mark */
  .brand {
    position: absolute;
    display: flex; align-items: center; gap: 10px;
    text-transform: uppercase; line-height: 1;
  }
  .brand__dot {
    width: 16px; height: 16px; border-radius: 50%;
    background: currentColor;
  }
  .label--compact .brand {
    top: 48px; left: 0; right: 0; justify-content: center;
    font-size: 30px;
  }
  .label--feature .brand {
    top: 42px; right: 33px;
    font-size: 50px;
  }

  /* origin */
  .origin { position: absolute; text-transform: uppercase; line-height: 1; }
  .origin__country { font-size: 29px; }
  .origin__variety { font-size: 20px; margin-top: 10px; }
  .label--compact .origin { top: 160px; left: 0; right: 0; text-align: center; }
  .label--feature .origin { top: 180px; right: 33px; text-align: right; }

  .rule { position: absolute; height: 1.5px; background: currentColor; width: 174px; }
  .label--compact .rule { left: 125px; }
  .label--feature .rule { right: 33px; }
  .label--compact .rule--top { top: 235px; }
  .label--compact .rule--bottom { top: 406px; }
  .label--feature .rule--top { top: 257px; }
  .label--feature .rule--bottom { top: 415px; }

  /* flavour scale */
  .profile {
    position: absolute;
    display: grid;
    grid-template-columns: 80px 100px;
    column-gap: 12px; row-gap: 15px;
    align-items: center;
  }
  .label--compact .profile { top: 256px; left: 115px; }
  .label--feature .profile { top: 277px; right: 33px; }
  .profile__name {
    text-align: right; font-size: 17px; text-transform: uppercase; line-height: 19px;
  }
  .scale { display: flex; gap: 6px; }
  .scale__step {
    width: 14px; height: 14px; border-radius: 50%;
    border: 1.5px solid currentColor;
  }
  .scale__step--on { background: currentColor; }

  /* pack details */
  .details {
    position: absolute;
    display: grid; grid-template-columns: auto 1.5px auto;
    column-gap: 10px;
    text-transform: uppercase; font-size: 17px; line-height: 25px;
  }
  .details__divider { background: currentColor; }
  .details__weight { text-align: right; padding: 8px 0; }
  .details__roast { text-align: left; padding: 8px 0; }
  .label--compact .details { top: 421px; left: 146px; height: 67px; }
  .label--feature .details { top: 434px; right: 33px; height: 66px; }

  /* character artwork area */
  .figure {
    position: absolute; left: 30px; top: 50px;
    width: 160px; height: 450px;
    border-radius: 80px 80px 18px 18px;
    z-index: 0;
  }
  .label--light .figure { background: linear-gradient(180deg, var(--figure-dark-a), var(--figure-dark-b)); }
  .label--dark .figure { background: linear-gradient(180deg, var(--figure-light-a), var(--figure-light-b)); }
</style>
</head>
<body>
<main class="sheet">

  <section class="label label--compact label--dark pos-tl">
    <div class="brand"><span class="brand__dot"></span><span class="brand__name">Amber Reed</span></div>
    <div class="origin"><p class="origin__country">Colombia</p><p class="origin__variety">Variety</p></div>
    <div class="rule rule--top"></div>
    <div class="profile">
      <span class="profile__name">Strength</span>
      <span class="scale"><i class="scale__step scale__step--on"></i><i class="scale__step scale__step--on"></i><i class="scale__step scale__step--on"></i><i class="scale__step"></i><i class="scale__step"></i></span>
      <span class="profile__name">Fruitiness</span>
      <span class="scale"><i class="scale__step scale__step--on"></i><i class="scale__step"></i><i class="scale__step"></i><i class="scale__step"></i><i class="scale__step"></i></span>
      <span class="profile__name">Earthiness</span>
      <span class="scale"><i class="scale__step scale__step--on"></i><i class="scale__step scale__step--on"></i><i class="scale__step scale__step--on"></i><i class="scale__step"></i><i class="scale__step"></i></span>
      <span class="profile__name">Brightness</span>
      <span class="scale"><i class="scale__step scale__step--on"></i><i class="scale__step scale__step--on"></i><i class="scale__step scale__step--on"></i><i class="scale__step"></i><i class="scale__step"></i></span>
    </div>
    <div class="rule rule--bottom"></div>
    <div class="details">
      <p class="details__weight">Weight<br>60 kg</p>
      <span class="details__divider"></span>
      <p class="details__roast">Roast date<br>20/2/2020</p>
    </div>
  </section>

  <section class="label label--compact label--light pos-tr">
    <div class="brand"><span class="brand__dot"></span><span class="brand__name">Amber Reed</span></div>
    <div class="origin"><p class="origin__country">Colombia</p><p class="origin__variety">Variety</p></div>
    <div class="rule rule--top"></div>
    <div class="profile">
      <span class="profile__name">Strength</span>
      <span class="scale"><i class="scale__step scale__step--on"></i><i class="scale__step scale__step--on"></i><i class="scale__step scale__step--on"></i><i class="scale__step"></i><i class="scale__step"></i></span>
      <span class="profile__name">Fruitiness</span>
      <span class="scale"><i class="scale__step scale__step--on"></i><i class="scale__step"></i><i class="scale__step"></i><i class="scale__step"></i><i class="scale__step"></i></span>
      <span class="profile__name">Earthiness</span>
      <span class="scale"><i class="scale__step scale__step--on"></i><i class="scale__step scale__step--on"></i><i class="scale__step scale__step--on"></i><i class="scale__step"></i><i class="scale__step"></i></span>
      <span class="profile__name">Brightness</span>
      <span class="scale"><i class="scale__step scale__step--on"></i><i class="scale__step scale__step--on"></i><i class="scale__step scale__step--on"></i><i class="scale__step"></i><i class="scale__step"></i></span>
    </div>
    <div class="rule rule--bottom"></div>
    <div class="details">
      <p class="details__weight">Weight<br>60 kg</p>
      <span class="details__divider"></span>
      <p class="details__roast">Roast date<br>20/2/2020</p>
    </div>
  </section>

  <section class="label label--feature label--light pos-bl">
    <div class="figure" role="img" aria-label="Silhouette character artwork holding a coffee cup"></div>
    <div class="brand"><span class="brand__name">Amber Reed</span></div>
    <div class="origin"><p class="origin__country">Colombia</p><p class="origin__variety">Variety</p></div>
    <div class="rule rule--top"></div>
    <div class="profile">
      <span class="profile__name">Strength</span>
      <span class="scale"><i class="scale__step scale__step--on"></i><i class="scale__step scale__step--on"></i><i class="scale__step scale__step--on"></i><i class="scale__step"></i><i class="scale__step"></i></span>
      <span class="profile__name">Fruitiness</span>
      <span class="scale"><i class="scale__step scale__step--on"></i><i class="scale__step"></i><i class="scale__step"></i><i class="scale__step"></i><i class="scale__step"></i></span>
      <span class="profile__name">Earthiness</span>
      <span class="scale"><i class="scale__step scale__step--on"></i><i class="scale__step scale__step--on"></i><i class="scale__step scale__step--on"></i><i class="scale__step"></i><i class="scale__step"></i></span>
      <span class="profile__name">Brightness</span>
      <span class="scale"><i class="scale__step scale__step--on"></i><i class="scale__step scale__step--on"></i><i class="scale__step scale__step--on"></i><i class="scale__step"></i><i class="scale__step"></i></span>
    </div>
    <div class="rule rule--bottom"></div>
    <div class="details">
      <p class="details__weight">Weight<br>60 kg</p>
      <span class="details__divider"></span>
      <p class="details__roast">Roast date<br>20/2/2020</p>
    </div>
  </section>

  <section class="label label--feature label--dark pos-br">
    <div class="figure" role="img" aria-label="Silhouette character artwork holding a coffee cup"></div>
    <div class="brand"><span class="brand__name">Amber Reed</span></div>
    <div class="origin"><p class="origin__country">Colombia</p><p class="origin__variety">Variety</p></div>
    <div class="rule rule--top"></div>
    <div class="profile">
      <span class="profile__name">Strength</span>
      <span class="scale"><i class="scale__step scale__step--on"></i><i class="scale__step scale__step--on"></i><i class="scale__step scale__step--on"></i><i class="scale__step"></i><i class="scale__step"></i></span>
      <span class="profile__name">Fruitiness</span>
      <span class="scale"><i class="scale__step scale__step--on"></i><i class="scale__step"></i><i class="scale__step"></i><i class="scale__step"></i><i class="scale__step"></i></span>
      <span class="profile__name">Earthiness</span>
      <span class="scale"><i class="scale__step scale__step--on"></i><i class="scale__step scale__step--on"></i><i class="scale__step scale__step--on"></i><i class="scale__step"></i><i class="scale__step"></i></span>
      <span class="profile__name">Brightness</span>
      <span class="scale"><i class="scale__step scale__step--on"></i><i class="scale__step scale__step--on"></i><i class="scale__step scale__step--on"></i><i class="scale__step"></i><i class="scale__step"></i></span>
    </div>
    <div class="rule rule--bottom"></div>
    <div class="details">
      <p class="details__weight">Weight<br>60 kg</p>
      <span class="details__divider"></span>
      <p class="details__roast">Roast date<br>20/2/2020</p>
    </div>
  </section>

</main>
</body>
</html>
```